Bussines Card - RM EDIFICACIONES, S.A.

We need a design for a business card.
I want it to look professional, but not old fashion.
We are like "young people', somehow i want it to look fresh, new, different, but still serious and professional.
I could use, a non typical design. (I mean, not just rectangular design).

The company Name is " RM EDIFICACIONES, S.A. " we are Panamenian company (spanish language) dedicated to construction and civil engeniering.

The company logo is attached, i use it with white background. Im not sure trying different one, could try.

```html
<!DOCTYPE html>
<html lang="es">
<head>
<meta charset="utf-8">
<title>RM Edificaciones – Tarjeta de presentación</title>
<link href="https://fonts.googleapis.com/css2?family=Exo+2:wght@400;500;700&display=swap" rel="stylesheet">
<style>
  :root{
    --bg:#ece9e4;
    --card-front:#ffffff;
    --card-back:#5e5e5e;
    --ink:#2b2b2b;
    --ink-soft:#4a4a4a;
    --icon-bg:#3a3a3a;
    --icon-fg:#ffffff;
  }
  *{box-sizing:border-box;margin:0;padding:0}
  html,body{width:1200px;height:672px;overflow:hidden}
  body{
    background:var(--bg);
    font-family:"Exo 2",sans-serif;
    color:var(--ink);
    display:flex;align-items:center;justify-content:center;gap:70px;
  }
  .card{
    width:330px;height:576px;
    box-shadow:0 10px 30px rgba(0,0,0,.18);
  }
  .card-back{background:var(--card-back)}
  .card-front{
    background:var(--card-front);
    position:relative;
    padding:0 36px;
  }
  .brand{
    position:absolute;top:78px;left:0;right:0;
    display:flex;flex-direction:column;align-items:center;
  }
  .brand-mark{width:92px;height:92px;background:var(--ink-soft)}
  .brand-name{
    margin-top:18px;
    font-weight:500;font-size:17px;letter-spacing:2px;color:var(--ink-soft);
  }
  .person{position:absolute;top:300px;left:36px}
  .person-name{font-weight:700;font-size:28px;letter-spacing:.5px;line-height:1}
  .person-role{font-size:11px;letter-spacing:1px;margin-top:4px;color:var(--ink-soft)}
  .contacts{position:absolute;top:366px;left:36px;list-style:none}
  .contact{display:flex;align-items:center;gap:10px;margin-bottom:9px;font-size:13px;line-height:1.2}
  .contact-icon{
    width:22px;height:22px;border-radius:3px;background:var(--icon-bg);
    display:flex;align-items:center;justify-content:center;flex-shrink:0;
  }
  .contact-icon svg{width:13px;height:13px;fill:var(--icon-fg)}
</style>
</head>
<body>
  <section class="card card-front">
    <div class="brand">
      <div class="brand-mark"></div>
      <div class="brand-name">RM EDIFICACIONES</div>
    </div>
    <div class="person">
      <h1 class="person-name">DIEGO MARÍN</h1>
      <p class="person-role">GENERAL MANAGER</p>
    </div>
    <ul class="contacts">
      <li class="contact">
        <span class="contact-icon"><svg viewBox="0 0 24 24"><path d="M6.6 10.8a15 15 0 0 0 6.6 6.6l2.2-2.2c.3-.3.7-.4 1-.2 1.1.4 2.3.6 3.6.6.6 0 1 .4 1 1V20c0 .6-.4 1-1 1A17 17 0 0 1 3 4c0-.6.4-1 1-1h3.5c.6 0 1 .4 1 1 0 1.3.2 2.5.6 3.6.1.3 0 .7-.2 1z"/></svg></span>
        <span>507 264 8130</span>
      </li>
      <li class="contact">
        <span class="contact-icon"><svg viewBox="0 0 24 24"><path d="M7 2h10a2 2 0 0 1 2 2v16a2 2 0 0 1-2 2H7a2 2 0 0 1-2-2V4a2 2 0 0 1 2-2zm0 3v13h10V5z"/></svg></span>
        <span>507 264 8131</span>
      </li>
      <li class="contact">
        <span class="contact-icon"><svg viewBox="0 0 24 24"><path d="M2 5h20v14H2zm2 2v.5l8 5 8-5V7zm0 3v7h16v-7l-8 5z"/></svg></span>
        <span>dmarin@rmedifica.com</span>
      </li>
      <li class="contact">
        <span class="contact-icon"><svg viewBox="0 0 24 24"><path d="M12 2a10 10 0 1 0 0 20 10 10 0 0 0 0-20zm0 2c1 1.3 1.8 3 2.1 5H9.9C10.2 7 11 5.3 12 4zM4.3 11h3.6c0 .7.1 1.4.2 2H4.3a8 8 0 0 1 0-2zm5.6 0h4.2a15 15 0 0 1 0 2H9.9a15 15 0 0 1 0-2zm6.2 0h3.6a8 8 0 0 1 0 2h-3.6c.1-.6.1-1.3 0-2zM12 20c-1-1.3-1.8-3-2.1-5h4.2c-.3 2-1.1 3.7-2.1 5z"/></svg></span>
        <span>www.rmedifica-pa.com</span>
      </li>
      <li class="contact">
        <span class="contact-icon"><svg viewBox="0 0 24 24"><path d="M12 2a7 7 0 0 0-7 7c0 5 7 13 7 13s7-8 7-13a7 7 0 0 0-7-7zm0 9.5a2.5 2.5 0 1 1 0-5 2.5 2.5 0 0 1 0 5z"/></svg></span>
        <span>Calle 50, Piso 12<br>Torre Norte, Panamá</span>
      </li>
    </ul>
  </section>
  <section class="card card-back" aria-label="Reverso de la tarjeta"></section>
</body>
</html>
```